Corporate Company Needs 3-series Flyer Template for Print

Flyer Contest Brief - We need a series of 3 templates to market and communicate our company’s leadership development program, using our corporate design elements. All 3 templates should have similar style, color, and elements --- but be noticeably different.

Template #1 – We need one template to communicate the Program Overview. It will include sections such as: learning objectives, descriptions about the online classes, a summary of required project, and the goals and purpose of the program

Template #2 – We need one template to communicate the details of an “Opening Event”. This template should include sections such as: Event location, event time, flight and hotel recommendations, event agenda, etc.

Template #3 - We need one template to communicate the details of an “Closing/Graduation Event”. This template should include sections such as: Event location, event time, flight and hotel recommendations, event agenda, etc.

Usage: We will edit and use the flyers to communicate our program, update information in the flyer and email the flyer to participants with each new class.

Our corporate design elements: Please refer to the attached PowerPoint file that includes a logo for the program, called KESTREL, and the purple brand color used for the program.

Size: Each template should be 8.5 x 11 inches

Look And Feel: Bold, Modern, Professional

File Type: Because I will edit, I need the flyer to be created in Microsoft Publisher or PowerPoint.

About the Program: The program is called KESTREL. It stands for Keystone Executive Strategy Track for Rising Emerging Leaders. This program is a high profile executive leadership course that lasts for approximately 5 months. Participants attend a live opening event and a live closing / graduation event. Over the course of 5 months the coursework includes: attending online classrooms, regional meetings, e-Learning classes, and manage a project. It is an exclusive program for high profile professional speakers, and it's important for the flyer to be engaging, professional, and clean.

I will need to be able to make small edits back and forth with the successful designer in order to get it just-right. This may only be possibly 2-3 rounds of edits.

Target Market(s)

Professional Executive Leaders in my company. Company is Harbinwell Partners, USA.

Industry/Entity Type

It Company

Colors
6b449b
0792cd
00a990
add136
fbf289
f04a50

Requirements
Must have
• I must be able to edit all elements of the 3 templates. Therefore, it must be in PowerPoint or Publisher. The designs must use our logo and our purple brand color.
Nice to have
• It would be nice if the designer used the colors provided in the PowerPoint file. It would be nice to see icons used creatively.
Should not have
• Design should not have fancy text or use pictures of people.

```html
<!DOCTYPE html>
<html lang="en">
<head>
<meta charset="utf-8">
<title>KESTREL – Learning Objectives</title>
<link rel="stylesheet" href="https://fonts.googleapis.com/css2?family=Catamaran:wght@400;500;600;700;800&display=swap">
<style>
  :root {
    --brand-purple: #6b449b;
    --deep-purple: #4a1250;
    --band-purple: #7a2a86;
    --ink: #2b2b2b;
    --grey-ink: #444444;
    --wall-light: #f4f4f4;
    --wall-mid: #e2e2e2;
    --panel-top: #d9cde8;
    --panel-bottom: #8e6bb8;
  }
  html, body { margin: 0; padding: 0; overflow: hidden; }
  body { width: 927px; height: 1200px; background: #fff; }
  .flyer {
    position: relative; width: 927px; height: 1200px; overflow: hidden;
    background: radial-gradient(ellipse at 40% 35%, var(--wall-light) 0%, #ececec 60%, var(--wall-mid) 100%);
    font-family: "Catamaran", sans-serif; color: var(--ink);
  }

  .brand { position: absolute; left: 274px; top: 92px; }
  .brand-row { display: flex; align-items: center; gap: 14px; }
  .brand-square { width: 62px; height: 62px; background: var(--brand-purple); flex: none; }
  .brand-name {
    font-family: "Catamaran", sans-serif; font-weight: 500; font-size: 92px;
    line-height: 1; color: var(--ink); letter-spacing: -1px;
  }
  .brand-tagline {
    margin-top: 8px; font-size: 10.5px; font-weight: 600; text-transform: uppercase;
    color: var(--brand-purple); white-space: nowrap;
  }

  .headline {
    position: absolute; left: 38px; top: 378px; margin: 0;
    font-family: "Catamaran", sans-serif; font-weight: 800; line-height: 0.95;
  }
  .headline-top { display: block; font-size: 74px; color: var(--brand-purple); letter-spacing: 4px; }
  .headline-bottom { display: block; font-size: 74px; color: var(--grey-ink); letter-spacing: 1px; }

  .objectives {
    position: absolute; left: 38px; top: 552px; width: 396px;
    margin: 0; padding: 0; list-style: none;
  }
  .objectives li {
    position: relative; padding-left: 26px; margin-bottom: 8px;
    font-size: 16.5px; line-height: 23px; color: var(--ink);
  }
  .objectives .tick { position: absolute; left: 0; top: 5px; width: 15px; height: 13px; }

  .feature-image {
    position: absolute; left: 470px; top: 216px; width: 410px; height: 984px; z-index: 2;
    border-radius: 180px 180px 0 0;
    background: linear-gradient(180deg, var(--panel-top) 0%, var(--panel-bottom) 100%);
  }

  .contact-top {
    position: absolute; left: 0; top: 1032px; width: 927px; height: 68px;
    background: var(--deep-purple); display: flex; align-items: center;
  }
  .contact-bottom {
    position: absolute; left: 0; top: 1100px; width: 927px; height: 100px;
    background: var(--band-purple); display: flex; align-items: center;
  }
  .contact-item {
    display: flex; align-items: center; gap: 16px; padding-left: 40px;
    font-family: "Catamaran", sans-serif; font-weight: 700; color: #fff;
  }
  .contact-top .contact-item { font-size: 40px; line-height: 1; }
  .contact-bottom .contact-item { font-size: 34px; line-height: 1; margin-top: -22px; }
  .contact-icon { width: 16px; height: 16px; flex: none; }
</style>
</head>
<body>
<div class="flyer">
  <header class="brand">
    <div class="brand-row">
      <span class="brand-square"></span>
      <span class="brand-name">kestrel</span>
    </div>
    <div class="brand-tagline">Keystone Executive Strategy Track for Rising Emerging Leaders</div>
  </header>

  <h1 class="headline">
    <span class="headline-top">LEARNING</span>
    <span class="headline-bottom">OBJECTIVES</span>
  </h1>

  <ul class="objectives">
    <li><svg class="tick" viewBox="0 0 15 13"><path d="M1 7 L5 11 L14 1" fill="none" stroke="#6b449b" stroke-width="2.6" stroke-linecap="round" stroke-linejoin="round"/></svg>During the program, there are five (5) mandatory MeetWave online classes. More than one scheduled date/time will be available for each topic. KESTREL participants will select the date/time preferred, but must attend all five as a requirement for completing the program.</li>
    <li><svg class="tick" viewBox="0 0 15 13"><path d="M1 7 L5 11 L14 1" fill="none" stroke="#6b449b" stroke-width="2.6" stroke-linecap="round" stroke-linejoin="round"/></svg>District/Region Finances + Debrief on Situational Leadership</li>
    <li><svg class="tick" viewBox="0 0 15 13"><path d="M1 7 L5 11 L14 1" fill="none" stroke="#6b449b" stroke-width="2.6" stroke-linecap="round" stroke-linejoin="round"/></svg>Talent Management + Debrief on Northfield Leadership Journal article, 'Managing Oneself'</li>
    <li><svg class="tick" viewBox="0 0 15 13"><path d="M1 7 L5 11 L14 1" fill="none" stroke="#6b449b" stroke-width="2.6" stroke-linecap="round" stroke-linejoin="round"/></svg>Harbinwell Partners Sales Process + Debrief on Working From A Distance</li>
    <li><svg class="tick" viewBox="0 0 15 13"><path d="M1 7 L5 11 L14 1" fill="none" stroke="#6b449b" stroke-width="2.6" stroke-linecap="round" stroke-linejoin="round"/></svg>Legal and Contracts + Debrief on Northfield Leadership Journal article, 'Manage Your Energy, Not Your Time'</li>
    <li><svg class="tick" viewBox="0 0 15 13"><path d="M1 7 L5 11 L14 1" fill="none" stroke="#6b449b" stroke-width="2.6" stroke-linecap="round" stroke-linejoin="round"/></svg>Harbinwell Partners Corporate Finance + Debrief on Northfield Leadership Journal article, 'Who's Got The Monkey?'</li>
  </ul>

  <div class="contact-top">
    <div class="contact-item">
      <svg class="contact-icon" viewBox="0 0 16 16"><path d="M4 1 L6.5 4.5 L5 6.5 C6 9 7.5 10.5 9.5 11 L11.5 9.5 L15 12 L13 15 C7 15 1 9 1 3 Z" fill="#fff"/></svg>
      <span class="contact-text">0147 258 369</span>
    </div>
  </div>
  <div class="contact-bottom">
    <div class="contact-item">
      <svg class="contact-icon" viewBox="0 0 16 16"><rect x="1" y="3" width="14" height="10" fill="#fff"/><path d="M1 3 L8 9 L15 3" fill="none" stroke="#7a2a86" stroke-width="1.5"/></svg>
      <span class="contact-text">info@kestrelprogram.com</span>
    </div>
  </div>

  <div class="feature-image" role="img" aria-label="Program feature image area in brand purple tones"></div>
</div>
</body>
</html>
```